QV - menu design

Hi,

We require elegant menu design for upscale restaurant. Please find attached the logo and the menu items for your reference.

for inspiration, this is a good website: -
http://www.platewhisper.example/bellfoldnotes/about.php

We are very much open for Menu Size suggestions.

unfortunately the place is going under renovation, we don't have updated images to it. the closest look and feel to our place is http://varnelo.example ..

we are also open for creative options on the shape, the styles, etc. as long as it represents the fine dine feel ...

Thanks ...

Dear All,

We wouldlike to extend our apology for not being able to provide feedbacks on everysingle design. We were extremely busy and we have multiple contests opensimultaneously which makes the process even harder.

However,we would like to thank you all for the efforts you have put into designingour menu. It is very much appreciated …

We wishyou all success in your design ventures and we are quite positive that we willbe working with many of you on many projects in the soon future. 

Thanks & Regards,

TLG Team...

 

 

 

Industry/Entity Type

Restaurant

Requirements
Must have
• Please ensure that there are 'some' images in the menu ... this is very important.
Should not have
• IMPORTANT: -

1. Please DO NOT insert any currency sign to the menu
2. Please keep the prices of the menu at the end of the menu items descriptions NOT beside the menu item names. The font of the price should be similar to the menu item description and please DO NOT bold the numbers. the prices should be subtle.

Thank you ...

```html
<!DOCTYPE html>
<html lang="en">
<head>
<meta charset="utf-8">
<title>QV – The Breakfast Menu</title>
<link href="https://fonts.googleapis.com/css2?family=Bebas+Neue&display=swap" rel="stylesheet">
<style>
  :root {
    --bg: #333333;
    --gold: #a77909;
    --mark: #141414;
    --photo-warm: #6b4a1c;
    --photo-deep: #2a2118;
  }
  html, body {
    margin: 0;
    padding: 0;
    width: 848px;
    height: 1200px;
    overflow: hidden;
    background: var(--bg);
  }
  .menu-page {
    position: relative;
    width: 848px;
    height: 1200px;
    background: var(--bg);
    color: var(--gold);
    font-family: "Bebas Neue", "Oswald", sans-serif;
    text-transform: uppercase;
  }
  .menu-title {
    position: absolute;
    left: 42px;
    top: 22px;
    margin: 0;
    font-size: 108px;
    font-weight: 400;
    line-height: 1;
    letter-spacing: 0.5px;
  }
  .menu-item { position: absolute; left: 0; width: 848px; }
  .item-name {
    position: absolute;
    left: 61px;
    top: 0;
    margin: 0;
    font-size: 37px;
    font-weight: 400;
    line-height: 1;
  }
  .item-desc {
    position: absolute;
    left: 88px;
    top: 46px;
    margin: 0;
    font-size: 19px;
    line-height: 24px;
    white-space: nowrap;
  }
  .item-price {
    position: absolute;
    right: 57px;
    margin: 0;
    font-size: 19px;
    line-height: 1;
  }
  .dish-photo {
    position: absolute;
    left: 61px;
    top: 990px;
    width: 420px;
    height: 170px;
    border: 1px solid var(--gold);
    background: linear-gradient(135deg, var(--photo-warm), var(--photo-deep));
  }
  .brand {
    position: absolute;
    left: 520px;
    top: 1080px;
    display: flex;
    align-items: center;
    gap: 14px;
    color: var(--mark);
  }
  .brand-square {
    width: 34px;
    height: 34px;
    background: var(--mark);
  }
  .brand-name {
    font-size: 58px;
    line-height: 1;
    letter-spacing: 6px;
  }
</style>
</head>
<body>
<main class="menu-page">
  <h1 class="menu-title">The Breakfast</h1>

  <section class="menu-item" style="top:168px">
    <h2 class="item-name">Butter Croissant</h2>
    <p class="item-desc">Served plain with a selection of two jams, a vanilla custard cream, a chocolate cream and butter curls).</p>
    <p class="item-price" style="top:72px">36</p>
  </section>

  <section class="menu-item" style="top:271px">
    <h2 class="item-name" style="left:63px">Cheese Croissant</h2>
    <p class="item-desc">Crumbly freshly baked with cheese filling.</p>
    <p class="item-price" style="top:76px">29</p>
  </section>

  <section class="menu-item" style="top:379px">
    <h2 class="item-name">Daily Fresh Eggs</h2>
    <p class="item-desc">A choice of poached, scrambled, pan fried, omelet) all served with toasted bread, mushrooms, roasted<br>tomatoes and chicken sausages.</p>
    <p class="item-price" style="top:102px">59</p>
  </section>

  <section class="menu-item" style="top:519px">
    <h2 class="item-name">Healthy Time</h2>
    <p class="item-desc">One choice of hot beverage from our cafe served with fruit salad, natural yoghurt, whole wheat bread<br>vegetable sandwiches and sugar free biscuits selection.</p>
    <p class="item-price" style="top:102px">49</p>
  </section>

  <section class="menu-item" style="top:655px">
    <h2 class="item-name">Energy Time</h2>
    <p class="item-desc">One choice of hot beverage from our cafe served with finger chocolate muffins, poached egg with toasted<br>read and crispy beef bacon, crepe roll with goat cheese and honey and finger chocolate cream with salted<br>cookies.</p>
    <p class="item-price" style="top:127px">59</p>
  </section>

  <section class="menu-item" style="top:801px">
    <h2 class="item-name">Quill Vale Time</h2>
    <p class="item-desc">One choice of hot beverage from our cafe served with our selection of scones, smoked salmon and avocado<br>sandwich, roasted sausages sandwich, grilled vegetables sandwich, selection of our best biscuits.</p>
    <p class="item-price" style="top:127px">59</p>
  </section>

  <div class="dish-photo" role="img" aria-label="Photograph of a breakfast spread with croissants, eggs and coffee"></div>

  <div class="brand">
    <span class="brand-square"></span>
    <span class="brand-name">Quill Vale</span>
  </div>
</main>
</body>
</html>
```